High-end residential home builder needs a business card design

We need a new business card design for a small residential construction company based in Boise, Idaho. We specialize in building custom high-end homes and remodels, with a focus on great design and craftsmanship.

We would like to use our current logo, but open to new color suggestions.
Just looking for a clean, sharp, modern design that looks high-end.

Target Market(s)

Upscale clientele

Industry/Entity Type

Contractor

Contact Information for Business Card

Company: Stonefield Custom Builders
Name: Marcus Tilley
Phone number: 208 367 4120
Email: MarcusTilleySCB@mailbox-example.com
Website: Stonefieldcustombuilders-example.com

Font styles to use
Serif
Sans Serif

Requirements
Must have
• Company Logo
Company name
My name
My phone number
My email
Company website
Nice to have
• I have attached a few photos of cards that I really like.

```html
<!DOCTYPE html>
<html lang="en">
<head>
<meta charset="utf-8">
<title>Stonefield Custom Builders – Business Card</title>
<link rel="stylesheet" href="https://fonts.googleapis.com/css2?family=Poppins:wght@300;600;800&display=swap">
<style>
  :root {
    --page: #ffffff;
    --violet: #3e4173;
    --navy-panel: #303558;
    --navy-deep: #263256;
    --gold: #f2c232;
    --amber: #dc962a;
    --white: #ffffff;
  }
  * { margin: 0; padding: 0; box-sizing: border-box; }
  html, body {
    width: 1200px; height: 1200px; overflow: hidden;
    background: var(--page);
    font-family: "Poppins", sans-serif;
  }
  .card {
    position: absolute; left: 109px; width: 972px; height: 538px;
    background: var(--violet); overflow: hidden;
  }
  .card--front { top: 49px; }
  .card--back { top: 619px; }
  .card__shapes { position: absolute; inset: 0; width: 972px; height: 538px; }

  .holder-name {
    position: absolute; left: 35px; top: 96px;
    font-weight: 800; font-size: 50px; color: var(--gold);
    letter-spacing: -0.5px; line-height: 1;
  }
  .company-label {
    position: absolute; left: 35px; top: 174px;
    font-weight: 600; font-size: 23px; color: var(--amber); line-height: 1;
  }
  .company-name {
    position: absolute; left: 35px; top: 203px;
    font-weight: 300; font-size: 23px; color: var(--amber); line-height: 1;
  }
  .contact-list { position: absolute; left: 62px; top: 317px; list-style: none; }
  .contact-item {
    display: flex; align-items: center; height: 40px; margin-bottom: 24px;
    font-weight: 600; font-size: 19px; color: var(--gold);
  }
  .contact-item__icon {
    width: 40px; height: 40px; border-radius: 50%;
    background: var(--amber); margin-right: 11px; flex: none;
    display: flex; align-items: center; justify-content: center;
  }
  .contact-item__icon svg { width: 22px; height: 22px; }

  .wordmark {
    position: absolute; text-align: center; color: var(--gold);
    font-weight: 600; line-height: 1;
  }
  .wordmark__mark {
    display: block; margin: 0 auto 26px;
    width: 64px; height: 64px; border: 4px solid var(--gold);
  }
  .wordmark__primary {
    display: block; font-size: 25px; letter-spacing: 0.45em; padding-left: 0.45em;
  }
  .wordmark__secondary {
    display: block; margin-top: 18px; font-size: 15px;
    letter-spacing: 0.5em; padding-left: 0.5em;
  }
  .card--front .wordmark { left: 542px; width: 400px; top: 205px; }
  .card--back .wordmark { left: 285px; width: 400px; top: 225px; }
</style>
</head>
<body>

<section class="card card--front" aria-label="Business card front">
  <svg class="card__shapes" viewBox="0 0 972 538" aria-hidden="true">
    <path fill="var(--navy-panel)" d="M0 0 H469 L544 42 Q568 56 568 82 V470 Q568 498 544 512 L501 538 H0 Z"/>
    <path fill="none" stroke="var(--white)" stroke-width="2" d="M510 22 L544 42 Q568 56 568 82 V470 Q568 498 544 512 L510 531"/>
  </svg>

  <h1 class="holder-name">Marcus Tilley</h1>
  <p class="company-label">Company:</p>
  <p class="company-name">Stonefield Custom Builders</p>

  <ul class="contact-list">
    <li class="contact-item">
      <span class="contact-item__icon">
        <svg viewBox="0 0 24 24" fill="none" stroke="var(--white)" stroke-width="1.5" stroke-linejoin="round">
          <path d="M5 3 L8 3 L10 7 L8 9 Q10 14 15 16 L17 14 L21 16 L21 19 Q20 21 17 21 Q5 18 3 6 Q3 3 5 3 Z"/>
        </svg>
      </span>
      208 367 4120
    </li>
    <li class="contact-item">
      <span class="contact-item__icon">
        <svg viewBox="0 0 24 24" fill="none" stroke="var(--white)" stroke-width="1.5">
          <rect x="2" y="5" width="20" height="14"/>
          <path d="M2 5 L12 13 L22 5 M2 19 L9 11 M22 19 L15 11"/>
        </svg>
      </span>
      MarcusTilleySCB@mailbox-example.com
    </li>
    <li class="contact-item">
      <span class="contact-item__icon">
        <svg viewBox="0 0 24 24" fill="none" stroke="var(--white)" stroke-width="1.3">
          <circle cx="12" cy="12" r="9"/>
          <ellipse cx="12" cy="12" rx="4" ry="9"/>
          <path d="M3 12 H21 M4.5 7.5 H19.5 M4.5 16.5 H19.5"/>
        </svg>
      </span>
      Stonefieldcustombuilders-example.com
    </li>
  </ul>

  <div class="wordmark">
    <span class="wordmark__mark"></span>
    <span class="wordmark__primary">STONEFIELD</span>
    <span class="wordmark__secondary">CUSTOM BUILDERS</span>
  </div>
</section>

<section class="card card--back" aria-label="Business card back">
  <svg class="card__shapes" viewBox="0 0 972 538" aria-hidden="true">
    <path fill="var(--navy-deep)" d="M194 0 H776 L838 36 Q863 52 863 78 V459 Q863 488 838 502 L776 538 H194 L131 502 Q106 488 106 459 V78 Q106 52 131 36 Z"/>
    <rect fill="var(--navy-panel)" x="285" y="62" width="400" height="412" rx="26"/>
  </svg>

  <div class="wordmark">
    <span class="wordmark__mark"></span>
    <span class="wordmark__primary">STONEFIELD</span>
    <span class="wordmark__secondary">CUSTOM BUILDERS</span>
  </div>
</section>

</body>
</html>
```